Flyer for cleaning services with special cut and space for general awareness

We need one flyer for cleaning services marketing. Its 2 page flyer preferred to have a special design [attracting people] . Colours should be from our brand guidelines.
We need a space in the flyer to paste one small ' hand wipes' with a general awareness of cleanliness.This flyer can be DL size . But we prefer to have a special design cut which attract people
Our services are
Office /Residential cleaning services
Deep cleaning
Move in /Move out
Carpet shampooing
Villa general cleaning
Apartment general cleaning
Event cleaning

Target Market(s)

Dubai

Industry/Entity Type

Cleaning Service

Font styles to use
Serif
Sans Serif

Requirements
Must have
• Brand guideline colours ,our staff photos
Nice to have
• Special design. cut [for Eg: shape of some cleaning equip]

```html
<!DOCTYPE html>
<html lang="en">
<head>
<meta charset="utf-8">
<title>Gulfshine Facilities – Cleaning Services Flyers</title>
<link href="https://fonts.googleapis.com/css2?family=Nunito+Sans:wght@400;700;800;900&family=Oswald:wght@500;600&family=Source+Sans+3:wght@400;600&display=swap" rel="stylesheet">
<style>
  :root{
    --navy:#1f2a7a;
    --purple:#6a3fa3;
    --violet:#8a5bc4;
    --blue:#2a8fd6;
    --sky:#e9eefa;
    --yellow:#fcd30f;
    --ink:#1b2260;
    --grey:#505463;
    --white:#ffffff;
    --stage:#e8e9ee;
  }
  *{margin:0;padding:0;box-sizing:border-box}
  html,body{width:1200px;height:749px;overflow:hidden;background:var(--stage)}
  .canvas{position:relative;width:1200px;height:749px}
  .flyer{position:absolute;top:48px;width:502px;height:649px;box-shadow:0 3px 10px rgba(0,0,0,.18);background:var(--white)}
  .flyer--left{left:59px}
  .flyer--right{left:644px}
  .flyer svg{display:block;width:100%;height:100%}

  .f-white{fill:var(--white)}
  .f-navy{fill:var(--navy)}
  .f-purple{fill:var(--purple)}
  .f-blue{fill:var(--blue)}
  .f-yellow{fill:var(--yellow)}
  .s-blue{stroke:var(--blue);fill:none}
  .s-purple{stroke:var(--purple);fill:none}

  .brand-name{font-family:"Nunito Sans",sans-serif;font-weight:800;font-size:23px;fill:var(--ink)}
  .headline{font-family:"Nunito Sans",sans-serif;font-weight:900;font-size:27px;fill:var(--ink)}
  .pill-text{font-family:"Nunito Sans",sans-serif;font-weight:800;font-size:22px;fill:var(--white)}
  .service{font-family:"Source Sans 3",sans-serif;font-weight:400;font-size:21px;fill:var(--grey)}
  .service-label{font-family:"Source Sans 3",sans-serif;font-weight:600;font-size:16px;fill:var(--grey)}
  .price-small{font-family:"Oswald",sans-serif;font-weight:600;font-size:13px;fill:var(--ink)}
  .price-big{font-family:"Oswald",sans-serif;font-weight:600;font-size:60px;fill:var(--ink)}
  .price-unit{font-family:"Oswald",sans-serif;font-weight:600;font-size:30px;fill:var(--ink)}
  .price-note{font-family:"Oswald",sans-serif;font-weight:500;font-size:14px;fill:var(--ink)}
  .tag-text{font-family:"Oswald",sans-serif;font-weight:500;font-size:12px;fill:var(--white)}
  .contact{font-family:"Oswald",sans-serif;font-weight:500;font-size:15px;fill:var(--white)}
</style>
</head>
<body>
<main class="canvas">

  <!-- Flyer one: list layout -->
  <section class="flyer flyer--left">
    <svg viewBox="0 0 614 794" xmlns="http://www.w3.org/2000/svg">
      <defs>
        <linearGradient id="photoKitchen" x1="0" y1="0" x2="1" y2="1">
          <stop offset="0" stop-color="#dfe3e8"/><stop offset=".55" stop-color="#b9bfc7"/><stop offset="1" stop-color="#7d8493"/>
        </linearGradient>
        <linearGradient id="photoStaff" x1="0" y1="0" x2="1" y2="1">
          <stop offset="0" stop-color="#e6ecf4"/><stop offset="1" stop-color="#5a6688"/>
        </linearGradient>
        <linearGradient id="bodyTint" x1="0" y1="0" x2="1" y2="0">
          <stop offset="0" stop-color="#ffffff"/><stop offset="1" stop-color="#e3e8f7"/>
        </linearGradient>
        <linearGradient id="footerBand" x1="0" y1="0" x2="1" y2="0">
          <stop offset="0" stop-color="#7a4fc0"/><stop offset="1" stop-color="#4b63c7"/>
        </linearGradient>
        <clipPath id="lc1"><circle cx="513" cy="347" r="68"/></clipPath>
        <clipPath id="lc2"><circle cx="513" cy="510" r="68"/></clipPath>
        <clipPath id="lc3"><circle cx="513" cy="677" r="68"/></clipPath>
      </defs>

      <rect class="photo" x="0" y="0" width="614" height="420" fill="url(#photoKitchen)" role="img" aria-label="Photo of a smiling staff member in uniform holding a caddy of cleaning products in a bright kitchen"/>

      <path class="header-swoosh" d="M0,0 H372 Q330,95 0,110 Z" class="f-white" fill="#fff"/>
      <path d="M372,0 Q330,95 0,110" class="s-blue" stroke-width="6"/>

      <g class="brand">
        <rect x="22" y="22" width="40" height="48" rx="4" class="f-purple"/>
        <text x="72" y="58" class="brand-name">Gulfshine Facilities</text>
      </g>

      <path class="body-panel" d="M0,410 Q220,300 614,320 V794 H0 Z" fill="url(#bodyTint)"/>
      <path d="M0,398 Q220,290 614,308" class="s-purple" stroke-width="8"/>
      <path d="M0,410 Q220,302 614,320" class="s-blue" stroke-width="6"/>

      <g class="price-burst" transform="translate(107 275)">
        <rect x="-68" y="-68" width="136" height="136" class="f-yellow"/>
        <rect x="-68" y="-68" width="136" height="136" class="f-yellow" transform="rotate(22.5)"/>
        <rect x="-68" y="-68" width="136" height="136" class="f-yellow" transform="rotate(45)"/>
        <rect x="-68" y="-68" width="136" height="136" class="f-yellow" transform="rotate(67.5)"/>
        <text x="-2" y="-41" class="price-small" text-anchor="middle">AED</text>
        <text x="-57" y="20" class="price-big">29/</text>
        <text x="20" y="20" class="price-unit">HR</text>
        <text x="0" y="45" class="price-note" text-anchor="middle">NORMAL SERVICES</text>
      </g>

      <text x="32" y="393" class="headline">OFFICE /RESIDENTIAL</text>
      <text x="32" y="427" class="headline">CLEANING SERVICES</text>

      <path class="services-pill" d="M0,441 H320 Q340,441 340,463 Q340,485 320,485 H0 Z" class="f-purple" fill="#6a3fa3"/>
      <text x="32" y="471" class="pill-text">OUR SERVICES INCLUDE:</text>

      <g class="service-list">
        <g transform="translate(42 505)"><circle r="8" class="s-blue" stroke-width="2"/><path d="M-2,-4 L2,0 L-2,4" class="s-blue" stroke-width="2"/></g>
        <text x="61" y="513" class="service">DEEP CLEANING</text>
        <g transform="translate(42 539)"><circle r="8" class="s-blue" stroke-width="2"/><path d="M-2,-4 L2,0 L-2,4" class="s-blue" stroke-width="2"/></g>
        <text x="61" y="547" class="service">MOVE IN /MOVE OUT</text>
        <g transform="translate(42 573)"><circle r="8" class="s-blue" stroke-width="2"/><path d="M-2,-4 L2,0 L-2,4" class="s-blue" stroke-width="2"/></g>
        <text x="61" y="581" class="service">CARPET SHAMPOOING</text>
        <g transform="translate(42 607)"><circle r="8" class="s-blue" stroke-width="2"/><path d="M-2,-4 L2,0 L-2,4" class="s-blue" stroke-width="2"/></g>
        <text x="61" y="615" class="service">VILLA GENERAL CLEANING</text>
        <g transform="translate(42 641)"><circle r="8" class="s-blue" stroke-width="2"/><path d="M-2,-4 L2,0 L-2,4" class="s-blue" stroke-width="2"/></g>
        <text x="61" y="649" class="service">APARTMENT GENERAL CLEANING</text>
        <g transform="translate(42 675)"><circle r="8" class="s-blue" stroke-width="2"/><path d="M-2,-4 L2,0 L-2,4" class="s-blue" stroke-width="2"/></g>
        <text x="61" y="683" class="service">EVENT CLEANING</text>
      </g>

      <g class="feature-circle">
        <circle cx="513" cy="347" r="80" class="f-purple"/><circle cx="513" cy="347" r="74" class="f-blue"/><circle cx="513" cy="347" r="68" class="f-white"/>
        <rect x="445" y="279" width="136" height="136" fill="url(#photoStaff)" clip-path="url(#lc1)" role="img" aria-label="Photo of a staff member wiping a cabinet"/>
        <path d="M450,368 H552 Q560,378 552,388 H450 Z" class="f-purple"/>
        <text x="462" y="383" class="tag-text">PROFESIONAL</text>
      </g>
      <g class="feature-circle">
        <circle cx="513" cy="510" r="80" class="f-purple"/><circle cx="513" cy="510" r="74" class="f-blue"/><circle cx="513" cy="510" r="68" class="f-white"/>
        <rect x="445" y="442" width="136" height="136" fill="url(#photoStaff)" clip-path="url(#lc2)" role="img" aria-label="Photo of a staff member cleaning a glass door"/>
        <path d="M452,534 H552 Q560,544 552,554 H452 Z" class="f-purple"/>
        <text x="463" y="549" class="tag-text">AFORDABLE</text>
      </g>

      <path class="footer" d="M0,707 H300 Q335,707 360,740 Q382,765 420,765 H614 V794 H0 Z" fill="url(#footerBand)"/>
      <rect x="420" y="765" width="194" height="29" class="f-blue"/>

      <g class="feature-circle">
        <circle cx="513" cy="677" r="80" class="f-purple"/><circle cx="513" cy="677" r="74" class="f-blue"/><circle cx="513" cy="677" r="68" class="f-white"/>
        <rect x="445" y="609" width="136" height="136" fill="url(#photoStaff)" clip-path="url(#lc3)" role="img" aria-label="Photo of a staff member cleaning a window frame"/>
        <path d="M452,704 H552 Q560,714 552,724 H452 Z" class="f-purple"/>
        <text x="462" y="719" class="tag-text">FAST &amp; EFFECTIVE</text>
      </g>

      <g class="contact-row">
        <circle cx="31" cy="739" r="10" fill="none" stroke="#fff" stroke-width="2"/>
        <path d="M27,734 q-1,6 6,10 l2,-2 -2,-2 -2,1 q-2,-2 -2,-4 l1,-2 -2,-2 Z" class="f-white"/>
        <text x="51" y="745" class="contact">CALL NOW 050 4127735 OR 600 521048</text>
        <circle cx="31" cy="770" r="10" fill="none" stroke="#fff" stroke-width="2"/>
        <ellipse cx="31" cy="770" rx="4" ry="10" fill="none" stroke="#fff" stroke-width="1.5"/>
        <line x1="21" y1="770" x2="41" y2="770" stroke="#fff" stroke-width="1.5"/>
        <text x="51" y="776" class="contact">WWW.GULFSHINEFACILITIES.COM</text>
      </g>
      <g class="social" fill="none" stroke="#fff" stroke-width="1.5">
        <circle cx="474" cy="780" r="8"/><circle cx="505" cy="780" r="8"/><circle cx="536" cy="780" r="8"/><circle cx="567" cy="780" r="8"/>
      </g>
    </svg>
  </section>

  <!-- Flyer two: icon grid layout -->
  <section class="flyer flyer--right">
    <svg viewBox="0 0 614 794" xmlns="http://www.w3.org/2000/svg">
      <defs>
        <linearGradient id="photoOffice" x1="0" y1="0" x2="1" y2="1">
          <stop offset="0" stop-color="#eef1f4"/><stop offset=".5" stop-color="#c3c9d1"/><stop offset="1" stop-color="#8a93a3"/>
        </linearGradient>
        <linearGradient id="photoStaff2" x1="0" y1="0" x2="1" y2="1">
          <stop offset="0" stop-color="#e6ecf4"/><stop offset="1" stop-color="#4f5b7e"/>
        </linearGradient>
        <linearGradient id="bodyTint2" x1="0" y1="0" x2="1" y2="0">
          <stop offset="0" stop-color="#ffffff"/><stop offset="1" stop-color="#e3e8f7"/>
        </linearGradient>
        <linearGradient id="footerBand2" x1="0" y1="0" x2="1" y2="0">
          <stop offset="0" stop-color="#7a4fc0"/><stop offset="1" stop-color="#4b63c7"/>
        </linearGradient>
        <radialGradient id="iconDisc" cx=".4" cy=".35" r=".7">
          <stop offset="0" stop-color="#3b4fb8"/><stop offset="1" stop-color="#1f2a7a"/>
        </radialGradient>
        <clipPath id="rc1"><circle cx="323" cy="330" r="64"/></clipPath>
        <clipPath id="rc2"><circle cx="500" cy="317" r="72"/></clipPath>
      </defs>

      <rect x="0" y="0" width="614" height="410" fill="url(#photoOffice)" role="img" aria-label="Photo of a smiling staff member giving a thumbs up in a modern meeting room"/>

      <path d="M0,0 H372 Q330,95 0,110 Z" fill="#fff"/>
      <path d="M372,0 Q330,95 0,110" class="s-blue" stroke-width="6"/>
      <g class="brand">
        <rect x="22" y="22" width="40" height="48" rx="4" class="f-purple"/>
        <text x="72" y="58" class="brand-name">Gulfshine Facilities</text>
      </g>

      <path d="M0,400 Q300,330 614,400 V794 H0 Z" fill="url(#bodyTint2)"/>
      <path d="M0,388 Q300,318 614,388" class="s-purple" stroke-width="8"/>
      <path d="M0,400 Q300,330 614,400" class="s-blue" stroke-width="6"/>

      <g class="price-burst" transform="translate(95 322)">
        <rect x="-68" y="-68" width="136" height="136" class="f-yellow"/>
        <rect x="-68" y="-68" width="136" height="136" class="f-yellow" transform="rotate(22.5)"/>
        <rect x="-68" y="-68" width="136" height="136" class="f-yellow" transform="rotate(45)"/>
        <rect x="-68" y="-68" width="136" height="136" class="f-yellow" transform="rotate(67.5)"/>
        <text x="-2" y="-41" class="price-small" text-anchor="middle">AED</text>
        <text x="-57" y="20" class="price-big">29/</text>
        <text x="20" y="20" class="price-unit">HR</text>
        <text x="0" y="45" class="price-note" text-anchor="middle">NORMAL SERVICES</text>
      </g>

      <g class="feature-circle">
        <circle cx="323" cy="330" r="76" class="f-purple"/><circle cx="323" cy="330" r="70" class="f-blue"/><circle cx="323" cy="330" r="64" class="f-white"/>
        <rect x="259" y="266" width="128" height="128" fill="url(#photoStaff2)" clip-path="url(#rc1)" role="img" aria-label="Photo of a staff member wiping an office desk"/>
      </g>
      <g class="feature-circle">
        <circle cx="500" cy="317" r="84" class="f-purple"/><circle cx="500" cy="317" r="78" class="f-blue"/><circle cx="500" cy="317" r="72" class="f-white"/>
        <rect x="428" y="245" width="144" height="144" fill="url(#photoStaff2)" clip-path="url(#rc2)" role="img" aria-label="Photo of a staff member cleaning a television screen"/>
      </g>

      <text x="307" y="445" class="headline" text-anchor="middle">OFFICE /RESIDENTIAL CLEANING SERVICES</text>

      <g class="service-grid">
        <g transform="translate(121 507)">
          <circle r="37" fill="url(#iconDisc)"/>
          <circle r="10" class="f-white"/>
          <g stroke="#fff" stroke-width="3"><line x1="0" y1="-18" x2="0" y2="18"/><line x1="-18" y1="0" x2="18" y2="0"/><line x1="-13" y1="-13" x2="13" y2="13"/><line x1="-13" y1="13" x2="13" y2="-13"/></g>
        </g>
        <text x="121" y="566" class="service-label" text-anchor="middle">DEEP CLEANING</text>

        <g transform="translate(302 507)">
          <circle r="37" fill="url(#iconDisc)"/>
          <path d="M-17,-6 L0,-13 L17,-6 L17,12 L0,18 L-17,12 Z" class="f-white"/>
          <path d="M-17,-6 L0,1 L17,-6 M0,1 V18" stroke="#1f2a7a" stroke-width="2" fill="none"/>
        </g>
        <text x="302" y="566" class="service-label" text-anchor="middle">MOVE IN /MOVE OUT</text>

        <g transform="translate(480 507)">
          <circle r="37" fill="url(#iconDisc)"/>
          <path d="M-8,-14 H6 V-8 H-8 Z M-10,-6 H8 Q12,0 12,6 V20 H-12 V6 Q-12,0 -10,-6 Z" class="f-white"/>
          <circle cx="14" cy="-14" r="1.6" class="f-white"/><circle cx="18" cy="-10" r="1.6" class="f-white"/><circle cx="19" cy="-17" r="1.6" class="f-white"/>
        </g>
        <text x="480" y="566" class="service-label" text-anchor="middle">CARPET SHAMPOOING</text>

        <g transform="translate(121 620)">
          <circle r="37" fill="url(#iconDisc)"/>
          <path d="M0,-20 L22,0 H15 V18 H4 V6 H-4 V18 H-15 V0 H-22 Z" class="f-white"/>
        </g>
        <text x="121" y="680" class="service-label" text-anchor="middle">VILLA CLEANING</text>

        <g transform="translate(302 620)">
          <circle r="37" fill="url(#iconDisc)"/>
          <rect x="-18" y="-8" width="16" height="26" class="f-white"/>
          <rect x="2" y="-20" width="16" height="38" class="f-white"/>
          <g fill="#1f2a7a"><rect x="-14" y="-3" width="4" height="4"/><rect x="-8" y="-3" width="4" height="4"/><rect x="-14" y="5" width="4" height="4"/><rect x="-8" y="5" width="4" height="4"/><rect x="6" y="-14" width="4" height="4"/><rect x="12" y="-14" width="4" height="4"/><rect x="6" y="-6" width="4" height="4"/><rect x="12" y="-6" width="4" height="4"/><rect x="6" y="2" width="4" height="4"/><rect x="12" y="2" width="4" height="4"/></g>
        </g>
        <text x="302" y="680" class="service-label" text-anchor="middle">APARTMENT CLEANING</text>

        <g transform="translate(480 620)">
          <circle r="37" fill="url(#iconDisc)"/>
          <line x1="12" y1="-20" x2="0" y2="6" stroke="#fff" stroke-width="4"/>
          <path d="M-6,4 L8,10 L2,22 L-14,16 Z" class="f-white"/>
          <rect x="-20" y="-10" width="12" height="14" class="f-white"/>
        </g>
        <text x="480" y="680" class="service-label" text-anchor="middle">EVENT CLEANING</text>
      </g>

      <path d="M0,707 H300 Q335,707 360,740 Q382,765 420,765 H614 V794 H0 Z" fill="url(#footerBand2)"/>
      <rect x="420" y="765" width="194" height="29" class="f-blue"/>

      <g class="partner-badges" fill="#c9ccd6">
        <rect x="350" y="718" width="18" height="24" rx="2"/>
        <rect x="373" y="720" width="44" height="20" rx="2"/>
        <rect x="421" y="720" width="24" height="20" rx="2"/>
        <circle cx="462" cy="730" r="11"/>
        <circle cx="494" cy="730" r="11"/>
        <circle cx="525" cy="730" r="11"/>
        <rect x="553" y="719" width="40" height="22" rx="2"/>
      </g>

      <g class="contact-row">
        <circle cx="31" cy="739" r="10" fill="none" stroke="#fff" stroke-width="2"/>
        <path d="M27,734 q-1,6 6,10 l2,-2 -2,-2 -2,1 q-2,-2 -2,-4 l1,-2 -2,-2 Z" class="f-white"/>
        <text x="51" y="745" class="contact">CALL NOW 050 4127735 OR 600 521048</text>
        <circle cx="31" cy="770" r="10" fill="none" stroke="#fff" stroke-width="2"/>
        <ellipse cx="31" cy="770" rx="4" ry="10" fill="none" stroke="#fff" stroke-width="1.5"/>
        <line x1="21" y1="770" x2="41" y2="770" stroke="#fff" stroke-width="1.5"/>
        <text x="51" y="776" class="contact">WWW.GULFSHINEFACILITIES.COM</text>
      </g>
      <g class="social" fill="none" stroke="#fff" stroke-width="1.5">
        <circle cx="474" cy="780" r="8"/><circle cx="505" cy="780" r="8"/><circle cx="536" cy="780" r="8"/><circle cx="567" cy="780" r="8"/>
      </g>
    </svg>
  </section>

</main>
</body>
</html>
```